Criação de Kit com 6 Layouts de Post para Redes Sociais (Facebook, Instagram e etc) para Vertente & Horizonte
A empresa queria:
" E-COMMERCE DE ELETRONICOS (celulares ,computadores e acessorios) E EMPRESA DE DESENVOLVIMENTO WEB "

```html
<!DOCTYPE html>
<html lang="pt-BR">
<head>
<meta charset="UTF-8">
<title>Vertente &amp; Horizonte — Smartphones</title>
<link rel="stylesheet" href="https://fonts.googleapis.com/css2?family=Montserrat:wght@400;500;700;800&display=swap">
<style>
  :root {
    --bg-deep: #2a1db4;
    --bg-mid: #3d2fe0;
    --bg-light: #5a63f0;
    --white: #ffffff;
    --yellow: #f4c02f;
    --device-dark: #1b1f4a;
    --device-lilac: #b39ad6;
    --pedestal-top: #4a3ff0;
    --pedestal-side: #2b22b8;
  }
  * { margin: 0; padding: 0; box-sizing: border-box; }
  html, body { width: 1200px; height: 1200px; overflow: hidden; }
  body { font-family: "Montserrat", sans-serif; }

  .post {
    position: relative;
    width: 1200px;
    height: 1200px;
    overflow: hidden;
    background:
      radial-gradient(circle at 18% 30%, var(--bg-light) 0%, rgba(90,99,240,0) 45%),
      linear-gradient(135deg, var(--bg-mid) 0%, var(--bg-deep) 100%);
  }

  .kicker {
    position: absolute;
    left: 240px;
    top: 104px;
    color: var(--white);
    font-weight: 500;
    font-size: 38px;
    line-height: 40px;
    letter-spacing: 7px;
    text-transform: uppercase;
  }

  .headline {
    position: absolute;
    font-weight: 800;
    line-height: 1;
    letter-spacing: -6px;
  }
  .headline--smart { left: 222px; top: 168px; font-size: 212px; color: var(--white); }
  .headline--phones { left: 212px; top: 338px; font-size: 222px; color: var(--yellow); }

  .accent-line {
    position: absolute;
    width: 6px;
    background: var(--white);
  }
  .accent-line--top { left: 934px; top: 214px; height: 40px; background: var(--yellow); }
  .accent-line--left { left: 286px; top: 600px; height: 100px; }

  .pedestal { position: absolute; left: 350px; top: 740px; }

  .device-photo {
    position: absolute;
    left: 420px;
    top: 205px;
    width: 360px;
    height: 600px;
    border-radius: 48px;
    background: linear-gradient(100deg, var(--device-dark) 0%, #2d3a8f 42%, var(--device-lilac) 58%, #d9c6ee 100%);
    box-shadow: 0 30px 60px rgba(10, 5, 80, 0.45);
  }

  .brand {
    position: absolute;
    left: 0;
    top: 966px;
    width: 1200px;
    text-align: center;
    color: var(--white);
    font-weight: 800;
    font-size: 66px;
    letter-spacing: 4px;
    text-transform: uppercase;
  }

  .contacts {
    position: absolute;
    left: 0;
    top: 1110px;
    width: 1200px;
    display: flex;
    justify-content: center;
    gap: 56px;
    color: var(--white);
    font-size: 26px;
    font-weight: 400;
  }
  .contact { display: flex; align-items: center; gap: 10px; }
  .contact__icon { width: 26px; height: 26px; }
</style>
</head>
<body>
  <main class="post">
    <p class="kicker">Celulares com<br>sistema Orbis</p>

    <span class="accent-line accent-line--top"></span>
    <span class="accent-line accent-line--left"></span>

    <h1 class="headline headline--smart">smart</h1>
    <h1 class="headline headline--phones">phones</h1>

    <svg class="pedestal" width="520" height="140" viewBox="0 0 520 140" aria-hidden="true">
      <ellipse cx="260" cy="82" rx="256" ry="54" fill="var(--pedestal-side)"/>
      <rect x="4" y="50" width="512" height="32" fill="var(--pedestal-side)"/>
      <ellipse cx="260" cy="50" rx="256" ry="46" fill="var(--pedestal-top)"/>
    </svg>

    <div class="device-photo" role="img" aria-label="Foto de dois smartphones, um escuro de frente e um lilás de costas, sobre o pedestal"></div>

    <p class="brand">Vertente &amp; Horizonte</p>

    <footer class="contacts">
      <span class="contact">
        <svg class="contact__icon" viewBox="0 0 24 24" aria-hidden="true">
          <circle cx="12" cy="12" r="12" fill="var(--yellow)"/>
          <path d="M8.5 6.5l2 2-1.2 1.6a7 7 0 0 0 4.6 4.6l1.6-1.2 2 2-1.4 1.8c-4.6-.6-8.3-4.3-8.9-8.9z" fill="var(--bg-deep)"/>
        </svg>
        (00) 0000-0000
      </span>
      <span class="contact">
        <svg class="contact__icon" viewBox="0 0 24 24" aria-hidden="true">
          <circle cx="12" cy="12" r="12" fill="var(--yellow)"/>
          <rect x="8.5" y="5.5" width="7" height="13" rx="1.5" fill="none" stroke="var(--bg-deep)" stroke-width="1.8"/>
        </svg>
        (00) 0000-0000
      </span>
      <span class="contact">
        <svg class="contact__icon" viewBox="0 0 24 24" aria-hidden="true">
          <circle cx="12" cy="12" r="12" fill="var(--yellow)"/>
          <rect x="6" y="8" width="12" height="8.5" rx="1" fill="none" stroke="var(--bg-deep)" stroke-width="1.6"/>
          <path d="M6.5 8.5l5.5 4.2 5.5-4.2" fill="none" stroke="var(--bg-deep)" stroke-width="1.6"/>
        </svg>
        email@email.com.br
      </span>
    </footer>
  </main>
</body>
</html>
```